New custom software business needs a Wordpress site

We need a Wordpress site for a new company based out of Chicago called 'Vellora Consulting'. Using a mix of on and off-shore resources we build custom software solutions, mainly focusing on small to medium sized companies. We help our customers "aspire" to do great things.
We have a basic site up here: https://brindlewave.example/. We worked on the content for it but not the branding. For now, this houses all the pages (except for a Contact Us page we'll be adding soon) for the foreseeable future.
We also have a new logo (attached) that we'd like to base the styling/colors on.
Target Market(s)
Small to medium sized companies that require tech resources
Industry/Entity Type
Software
Nice to have
- Teamwork, tech, professional but not elitist

```html
<!DOCTYPE html>
<html lang="en">
<head>
<meta charset="utf-8">
<title>Vellora Consulting</title>
<link href="https://fonts.googleapis.com/css2?family=Orbitron:wght@500;600;700&family=Poppins:ital,wght@0,400;0,500;1,400&display=swap" rel="stylesheet">
<style>
:root{
  --primary:#0353a4;
  --mid:#3f7fc1;
  --soft:#e8f0f8;
  --ink:#2b2b2b;
  --grey:#6a6a6a;
  --white:#ffffff;
  --display:'Orbitron',sans-serif;
  --body:'Poppins',sans-serif;
}
*{margin:0;padding:0;box-sizing:border-box}
html,body{width:1200px;height:3518px;overflow:hidden;background:var(--white);font-family:var(--body);color:var(--ink)}
.page{position:relative;width:1200px;height:3518px}
.abs{position:absolute}
.site-header{left:0;top:0;width:1200px;height:90px;background:var(--white)}
.brand{left:61px;top:26px;display:flex;align-items:center;gap:10px}
.brand-mark{width:30px;height:30px;background:var(--primary)}
.brand-name{font-family:var(--body);font-weight:500;font-size:21px;color:var(--primary)}
.nav{right:60px;top:36px;display:flex;gap:29px;font-size:14px;color:var(--ink)}
.nav .active{color:var(--primary)}
.hero-left{left:0;top:90px;width:600px;height:599px;background:var(--soft)}
.hero-photo{left:600px;top:90px;width:600px;height:599px;background:linear-gradient(135deg,#8a8f96,#c98a4f 45%,#5c6b7a)}
.hero-title{left:61px;top:274px;font-family:var(--display);font-weight:600;font-size:52px;line-height:58px;color:var(--primary);letter-spacing:1px}
.hero-sub{left:61px;top:400px;font-size:17px;line-height:27px;color:var(--ink);width:470px}
.btn{display:flex;align-items:center;justify-content:center;font-family:var(--display);font-weight:600;letter-spacing:1px;color:var(--white);background:var(--mid)}
.hero-btn{left:60px;top:475px;width:168px;height:48px;font-size:17px}
.about{left:0;top:689px;width:1200px;height:413px;background:var(--primary);color:var(--white)}
.about-title{left:61px;top:768px;font-family:var(--display);font-weight:600;font-size:34px;color:var(--white);letter-spacing:1px}
.about-col{top:838px;width:345px;font-size:13.5px;line-height:22.5px;color:var(--white)}
.feature-photo{background:linear-gradient(135deg,#b9a792,#6f6a64 50%,#3d4a5a)}
.feature-title{font-family:var(--display);font-weight:600;font-size:33px;line-height:41px;color:var(--primary);letter-spacing:1px}
.feature-text{font-size:13.5px;line-height:25px;color:var(--grey)}
.provide{left:0;top:2115px;width:1200px;height:442px;background:var(--soft)}
.provide-title{left:0;top:2190px;width:1200px;text-align:center;font-family:var(--display);font-weight:600;font-size:34px;color:var(--primary);letter-spacing:1px}
.service{top:2264px;width:300px;text-align:center}
.service h3{margin-top:14px;font-family:var(--display);font-weight:600;font-size:17px;letter-spacing:1px;color:var(--ink)}
.service p{margin-top:14px;font-size:13.5px;line-height:21px;color:var(--ink)}
.testimonial{left:0;top:2557px;width:1200px;height:416px;background:linear-gradient(90deg,#0a4d9a,#0553a6 50%,#0a4d9a)}
.avatar{left:553px;top:2620px;width:104px;height:104px;border-radius:50%;background:linear-gradient(#e9edf1,#b9c2cc);border:3px solid var(--white)}
.quote{left:290px;top:2744px;width:620px;text-align:center;font-style:italic;font-size:17.5px;line-height:30px;color:var(--white)}
.cite{left:0;top:2866px;width:1200px;text-align:center;font-family:var(--display);font-size:16px;letter-spacing:1px;color:var(--white)}
.contact-photo{left:137px;top:3044px;width:409px;height:421px;background:linear-gradient(180deg,#ffffff,#cfdcea 40%,#9fb2c8)}
.contact-title{left:618px;top:3064px;font-family:var(--display);font-weight:600;font-size:35px;color:var(--primary);letter-spacing:1px}
.contact-sub{left:624px;top:3119px;font-size:16px;color:var(--grey)}
.contact-row{left:620px;display:flex;align-items:center;gap:18px;font-size:17px;color:var(--ink)}
.icon-circle{width:46px;height:46px;border-radius:50%;background:var(--mid);display:flex;align-items:center;justify-content:center}
.email-input{left:620px;top:3305px;width:286px;height:48px;border:1px solid var(--mid);background:var(--white);font-size:12px;color:var(--grey);padding:0 16px;display:flex;align-items:center}
.subscribe{left:906px;top:3305px;width:164px;height:48px;font-size:18px}
.footer{left:0;top:3465px;width:1200px;height:53px;background:var(--mid);color:var(--white);font-size:14px;display:flex;align-items:center;justify-content:center}
</style>
</head>
<body>
<div class="page">
  <header class="abs site-header">
    <div class="abs brand"><span class="brand-mark"></span><span class="brand-name">Vellora Consulting</span></div>
    <nav class="abs nav">
      <span class="active">Home</span><span>About</span><span>Services</span><span>Why Vellora?</span><span>Vellora Leadership</span><span>Contact Us</span>
    </nav>
  </header>

  <section>
    <div class="abs hero-left"></div>
    <div class="abs hero-photo" role="img" aria-label="Team of colleagues gathered around a tablet in a bright office"></div>
    <h1 class="abs hero-title">VELLORA<br>CONSULTING</h1>
    <p class="abs hero-sub">Using a mix of on and off-shore resources we build custom software solutions</p>
    <div class="abs btn hero-btn">CONTACT US</div>
    <svg class="abs" style="left:226px;top:475px" width="30" height="48"><polygon points="14,0 20,0 6,48 0,48" fill="var(--mid)"/></svg>
  </section>

  <section class="abs about"></section>
  <h2 class="abs about-title">VELLORA CONSULTING</h2>
  <p class="abs about-col" style="left:61px">Welcome to Vellora, a software consulting company specializing in serving small to medium size businesses. We understand the unique challenges and opportunities that these companies face, and we are dedicated to helping them succeed through innovative technology solutions.</p>
  <p class="abs about-col" style="left:429px">Our team of experienced professionals has a diverse range of skills and expertise, making us well-equipped to handle any project, big or small. We specialize in custom software development, working closely with our clients to understand their specific needs and build solutions that meet their requirements.</p>
  <p class="abs about-col" style="left:796px">From developing web and mobile applications to implementing cloud-based systems and integrating with existing platforms, we have the tools and knowledge to deliver results that drive success. We also offer a range of other services, including IT consulting, project management, and technical support, to help businesses optimize their operations and achieve their goals.</p>

  <section>
    <div class="abs feature-photo" style="left:60px;top:1188px;width:516px;height:368px;clip-path:polygon(0 0,516px 0,370px 368px,0 368px)" role="img" aria-label="Team meeting around a conference table"></div>
    <svg class="abs" style="left:60px;top:1188px" width="516" height="368"><polygon points="370,368 502,368 445,210" fill="var(--primary)"/></svg>
    <h2 class="abs feature-title" style="left:640px;top:1280px">CUSTOM SOLUTIONS<br>DELIVERY</h2>
    <p class="abs feature-text" style="left:640px;top:1376px;width:420px">Vellora offers a range of services focused on helping businesses and organizations deliver software solutions to their customers or users.</p>
  </section>

  <section>
    <div class="abs feature-photo" style="left:622px;top:1672px;width:518px;height:368px;clip-path:polygon(0 0,518px 0,518px 368px,149px 368px)" role="img" aria-label="Three colleagues reviewing documents at a desk"></div>
    <svg class="abs" style="left:622px;top:1672px" width="518" height="368"><polygon points="30,368 149,368 94,219" fill="var(--primary)"/></svg>
    <h2 class="abs feature-title" style="left:60px;top:1779px">STAFF<br>AUGMENTATION</h2>
    <p class="abs feature-text" style="left:61px;top:1871px;width:430px">Let Vellora help you supplement your existing software development teams with additional resources and expertise. We provided access to experienced</p>
  </section>

  <section class="abs provide"></section>
  <h2 class="abs provide-title">ALSO WE PROVIDE</h2>
  <div class="abs service" style="left:128px">
    <svg width="160" height="106" viewBox="0 0 160 106"><polygon points="80,2 154,106 6,106" fill="var(--white)"/><line x1="80" y1="2" x2="6" y2="106" stroke="#9dbfe3" stroke-width="3"/><g fill="none" stroke="var(--primary)" stroke-width="2.5"><circle cx="84" cy="60" r="9"/><circle cx="84" cy="84" r="6"/><rect x="58" y="40" width="16" height="11" rx="2"/><rect x="100" y="80" width="14" height="11" rx="2"/></g></svg>
    <h3>IT CONSULTING</h3><p>We help our customers "aspire" to do<br>great things.</p>
  </div>
  <div class="abs service" style="left:450px">
    <svg width="160" height="106" viewBox="0 0 160 106"><polygon points="80,2 154,106 6,106" fill="var(--white)"/><line x1="80" y1="2" x2="6" y2="106" stroke="#9dbfe3" stroke-width="3"/><g fill="none" stroke="var(--primary)" stroke-width="2.5"><rect x="56" y="46" width="46" height="32" rx="2"/><path d="M50 84h58"/><path d="M64 58h22M64 66h28"/><circle cx="98" cy="48" r="9"/></g></svg>
    <h3>PROJECT MANAGEMENT</h3><p>We help our customers "aspire" to do<br>great things.</p>
  </div>
  <div class="abs service" style="left:767px">
    <svg width="160" height="106" viewBox="0 0 160 106"><polygon points="80,2 154,106 6,106" fill="var(--white)"/><line x1="80" y1="2" x2="6" y2="106" stroke="#9dbfe3" stroke-width="3"/><g fill="none" stroke="var(--primary)" stroke-width="2.5"><path d="M60 70v-8a20 20 0 0 1 40 0v8"/><rect x="55" y="64" width="8" height="14" rx="3"/><rect x="97" y="64" width="8" height="14" rx="3"/><circle cx="80" cy="72" r="9"/><circle cx="90" cy="44" r="7"/></g></svg>
    <h3>TECHNICAL SUPPORT</h3><p>We help our customers "aspire" to do<br>great things.</p>
  </div>

  <section class="abs testimonial" role="img" aria-label="Blue-tinted office scene behind a client testimonial"></section>
  <div class="abs avatar" role="img" aria-label="Portrait of the quoted client"></div>
  <p class="abs quote">" Lorem Ipsum has been the industry's standard dummy text ever since the when an unknown printer took a galley of type &nbsp;scrait to has been the industry's standard dummy text ever since the &nbsp;"</p>
  <p class="abs cite">— MAREN ASHBY</p>

  <section>
    <div class="abs contact-photo" role="img" aria-label="Two professionals looking at a laptop together"></div>
    <h2 class="abs contact-title">GET IN TOUCH</h2>
    <p class="abs contact-sub">If you have an any question for contact us today !</p>
    <div class="abs contact-row" style="top:3172px">
      <span class="icon-circle"><svg width="22" height="22" viewBox="0 0 24 24" fill="none" stroke="#fff" stroke-width="1.6"><path d="M5 3h4l2 5-2.5 1.5a11 11 0 0 0 6 6L16 13l5 2v4a2 2 0 0 1-2 2A16 16 0 0 1 3 5a2 2 0 0 1 2-2z"/></svg></span>
      <span>0198 765 432</span>
    </div>
    <div class="abs contact-row" style="top:3230px">
      <span class="icon-circle"><svg width="22" height="22" viewBox="0 0 24 24" fill="none" stroke="#fff" stroke-width="1.6"><rect x="3" y="5" width="18" height="14" rx="1"/><path d="M3 6l9 7 9-7"/></svg></span>
      <span>info@VelloraConsulting.example</span>
    </div>
    <div class="abs email-input">Enter Email *</div>
    <div class="abs btn subscribe">SUBSCRIBE</div>
    <svg class="abs" style="left:1068px;top:3305px" width="26" height="48"><polygon points="16,0 22,0 6,48 0,48" fill="var(--mid)"/></svg>
  </section>

  <footer class="abs footer">©VelloraConsulting - 2022 All rights reserved.</footer>
</div>
</body>
</html>
```